Modern & Simple Essential Oils Label

Company Name: Verdant Hollow

What we sell: Aromatherapy products, pure therapeutic essential oils.

Design need:
We are looking for a creative and youthful design for the labels used on small essentials oils.

I have two sizes of bottles that I use for essential oils a 5ml bottle and a 15ml bottle. They are dark Amber color glass with black lids. I like the clear labels or mayble a dark brown background. With white or clear lettering with punch of color too! Each oil type is represented by different color. (lavender- purple, lemon - yellow). The label will be the same for all the oils in the two sizes with only a different oil name & coordinating color.
5ml label size should be: 1 " x 2.625"
15ml label size should be: 1.5" x 3.5"

I have some labels that I have had another designer start on, but they aren't quite what I want and missing that something (alot!).. I don't know what. Interest maybe? Lack of design? I dunno.. they are attached. Maybe it's the logo? I don't know! But its gotta change! When I cut out a proof and put a sample on the bottle as I look straight on at the label all I see is a big dot, no logo.. nothing interesting.
Updates

Project Deadline Extended
Reason: Hi! Id like to extend this deadline. Ive been unavailable for a few days due to an illness and Im so far behind! Im feeling MUCH better and looking forward to getting caught up and move with the project. Im not sure how this works, but I attached a list of the oils that we currently have available. And in the list is the idea for the color schemes for the oils. The basic idea is for it to have a wide array of colors, so using different shades of greens, yellows, oranges and so on. So that its like a rainbow. We are not set of that particular color for that particular oil. It was just a idea list of possible colors for oils. Thanks so much!

Target Market(s)

Metro & Modern people. Interested in healthy organic living, Mostly women (some men) 20-45 who are interested in holistic healing.

Industry/Entity Type

It Company

Requirements
Must have
• A reputable look. Clean, organic, crisp, zen or spa-like feel. Modern, youthful appealing label design. Approachable and interesting, not intimidating so that I don't turn away people who are new or not familiar with how to use essential oils.
Should not have
• do NOT want the look to be anywhere close to medicinal, witchy, crafty, hippie, mystical, overly earthy, magical, or voodoo. Do not want it to look like something out of a grandmothers medicine cabinet.

```html
<!DOCTYPE html>
<html lang="en">
<head>
<meta charset="utf-8">
<title>Verdant Hollow – Essential Oil Labels</title>
<link href="https://fonts.googleapis.com/css2?family=Arimo:wght@400;500&family=Open+Sans:wght@400;700&display=swap" rel="stylesheet">
<style>
  :root {
    --bg-center: #6e6e70;
    --bg-edge: #161617;
    --label-brown: #4a3a31;
    --label-white: #ffffff;
    --label-edge: #111111;
    --logo-ink: #4a3a32;
    --sandalwood: #f7d417;
    --chamomile: #e4477c;
    --rosemary: #4aa0a6;
    --tab-text: #ffffff;
  }
  * { margin: 0; padding: 0; box-sizing: border-box; }
  html, body { width: 1200px; height: 1000px; overflow: hidden; }
  body {
    position: relative;
    background: radial-gradient(ellipse at 50% 45%, var(--bg-center) 0%, #3a3a3c 45%, var(--bg-edge) 100%);
    font-family: "Arimo", Arial, sans-serif;
  }
  .label-art { position: absolute; left: 0; top: 0; }
  .brand {
    position: absolute;
    width: 220px;
    text-align: center;
    color: var(--logo-ink);
    font-family: "Arimo", Arial, sans-serif;
    font-weight: 500;
    font-size: 21px;
    line-height: 1.08;
    letter-spacing: 0.5px;
    text-transform: uppercase;
  }
  .brand-dot {
    display: block;
    width: 28px; height: 28px;
    margin: 0 auto 9px;
    border-radius: 50%;
    background: var(--logo-ink);
  }
  .oil { position: absolute; font-family: "Arimo", Arial, sans-serif; }
  .oil-name { font-size: 38px; line-height: 1; letter-spacing: 0.2px; }
  .oil-detail { font-size: 17px; line-height: 1.1; margin-top: 6px; }
  .oil--sandalwood { left: 772px; top: 268px; color: var(--sandalwood); }
  .oil--chamomile { left: 255px; top: 726px; color: var(--chamomile); }
  .oil--rosemary { left: 710px; top: 716px; color: var(--rosemary); }
  .oil--rosemary .oil-name { font-size: 44px; }
  .oil--rosemary .oil-detail { margin-top: 2px; font-size: 18px; line-height: 1.05; }

  .tab-text {
    position: absolute;
    color: var(--tab-text);
    font-family: "Open Sans", Arial, sans-serif;
    font-size: 13.5px;
    line-height: 15.5px;
  }
  .tab-facts { left: 173px; top: 244px; }
  .tab-maker { left: 409px; top: 244px; }
  .tab-maker strong { font-weight: 700; }
  .tab-maker .highlight { color: var(--sandalwood); }
  .tab-divider {
    position: absolute; left: 381px; top: 224px;
    width: 2px; height: 103px; background: var(--tab-text);
  }
  .tab-caution { left: 172px; top: 346px; width: 530px; }
</style>
</head>
<body>

<svg class="label-art" width="1200" height="1000" viewBox="0 0 1200 1000" xmlns="http://www.w3.org/2000/svg">
  <defs>
    <clipPath id="clip-sandalwood">
      <path d="M712,277 A169,174 0 1 1 881,451 L736,451 Q712,451 712,427 Z"/>
    </clipPath>
    <clipPath id="clip-tab">
      <rect x="142" y="222" width="600" height="190" rx="20"/>
    </clipPath>
    <clipPath id="clip-chamomile">
      <path d="M203,722 A169,178 0 1 1 372,900 L226,900 Q203,900 203,877 Z"/>
    </clipPath>
    <clipPath id="clip-rosemary">
      <path d="M662,722 A168,178 0 1 1 830,900 L685,900 Q662,900 662,877 Z"/>
    </clipPath>
    <linearGradient id="wood-tones" x1="0" y1="0" x2="1" y2="1">
      <stop offset="0" stop-color="#a9552b"/>
      <stop offset="0.5" stop-color="#c06a38"/>
      <stop offset="1" stop-color="#7a3a1d"/>
    </linearGradient>
    <linearGradient id="chamomile-tones" x1="0" y1="0" x2="1" y2="0">
      <stop offset="0" stop-color="#d9b54a"/>
      <stop offset="0.5" stop-color="#c9a35a"/>
      <stop offset="1" stop-color="#8c7a45"/>
    </linearGradient>
    <linearGradient id="rosemary-tones" x1="0" y1="0" x2="1" y2="0">
      <stop offset="0" stop-color="#4c6b3a"/>
      <stop offset="0.5" stop-color="#7a7fa8"/>
      <stop offset="1" stop-color="#5d7a4a"/>
    </linearGradient>
  </defs>

  <!-- 15 ml wrap label: info tab -->
  <g class="wrap-tab" clip-path="url(#clip-tab)">
    <rect x="142" y="222" width="600" height="190" fill="var(--label-brown)"/>
    <path d="M490,412 Q600,400 742,380 L742,412 Z" fill="url(#wood-tones)" role="img" aria-label="Sandalwood chips photo"/>
  </g>

  <!-- 15 ml wrap label: sandalwood face -->
  <g class="label-face label-face--sandalwood" clip-path="url(#clip-sandalwood)">
    <rect x="700" y="95" width="360" height="120" fill="var(--label-white)"/>
    <rect x="700" y="215" width="360" height="10" fill="var(--sandalwood)"/>
    <rect x="700" y="225" width="360" height="230" fill="var(--label-brown)"/>
    <path d="M700,412 Q860,400 1060,360 L1060,455 L700,455 Z" fill="url(#wood-tones)" role="img" aria-label="Sandalwood chips photo"/>
  </g>
  <path d="M712,277 A169,174 0 1 1 881,451 L736,451 Q712,451 712,427 Z" fill="none" stroke="var(--label-edge)" stroke-width="1.5"/>

  <!-- 5 ml label: chamomile -->
  <g class="label-face label-face--chamomile" clip-path="url(#clip-chamomile)">
    <rect x="195" y="540" width="350" height="125" fill="var(--label-white)"/>
    <rect x="195" y="665" width="350" height="12" fill="var(--chamomile)"/>
    <rect x="195" y="677" width="350" height="230" fill="var(--label-brown)"/>
    <path d="M195,852 Q380,860 545,825 L545,905 L195,905 Z" fill="url(#chamomile-tones)" role="img" aria-label="Dried chamomile flowers photo"/>
  </g>
  <path d="M203,722 A169,178 0 1 1 372,900 L226,900 Q203,900 203,877 Z" fill="none" stroke="var(--label-edge)" stroke-width="1.5"/>

  <!-- 5 ml label: rosemary -->
  <g class="label-face label-face--rosemary" clip-path="url(#clip-rosemary)">
    <rect x="655" y="540" width="350" height="124" fill="var(--label-white)"/>
    <rect x="655" y="664" width="350" height="10" fill="var(--rosemary)"/>
    <rect x="655" y="674" width="350" height="232" fill="var(--label-brown)"/>
    <path d="M655,848 Q830,858 1005,820 L1005,905 L655,905 Z" fill="url(#rosemary-tones)" role="img" aria-label="Rosemary sprigs with blossoms photo"/>
  </g>
  <path d="M662,722 A168,178 0 1 1 830,900 L685,900 Q662,900 662,877 Z" fill="none" stroke="var(--label-edge)" stroke-width="1.5"/>
</svg>

<!-- Brand marks -->
<div class="brand" style="left:771px; top:124px;"><span class="brand-dot"></span>Verdant<br>Hollow</div>
<div class="brand" style="left:256px; top:562px;"><span class="brand-dot"></span>Verdant<br>Hollow</div>
<div class="brand" style="left:717px; top:562px;"><span class="brand-dot"></span>Verdant<br>Hollow</div>

<!-- Oil faces -->
<div class="oil oil--sandalwood">
  <div class="oil-name">sandalwood</div>
  <div class="oil-detail">Santalum Album<br>100% Pure Essential Oil<br>15 ml</div>
</div>
<div class="oil oil--chamomile">
  <div class="oil-name">chamomile</div>
  <div class="oil-detail">Anthemis Nobilis<br>100% Pure Essential Oil</div>
</div>
<div class="oil oil--rosemary">
  <div class="oil-name">rosemary</div>
  <div class="oil-detail">Rosmarinus Officinalis<br>100% Pure Essential Oil</div>
</div>

<!-- Info tab text -->
<div class="tab-text tab-facts">
  Supplemental Facts<br>
  Serving Size: 1 drop<br>
  Servings per Container:<br>
  About 250<br>
  Oil: Anthemis Nobilis
</div>
<div class="tab-divider"></div>
<div class="tab-text tab-maker">
  <strong>Verdant Hollow</strong><br>
  P.O. Box 402, Fairmont, OR 97321<br>
  For aromatic, topical use.<br>
  <span class="highlight">100% pure therapeutic-grade essential oil.</span><br>
  Dilute with a carrier oil before using.
</div>
<div class="tab-text tab-caution">
  CAUTION: For External Use Only. Not for Ingestion. Keep away from eyes and mucous membranes. May cause skin sensitivity. If pregnant consult physician before use. Keep out of reach of children. Keep away from flame.
</div>

</body>
</html>
```